Flyer for an online formula one racing league

Hello.

I am looking for the perfect one page facebook/instagram style flyer for an online formula one racing league. The racing league is called 'VOLTA RACING LEAGUE'.

Information that MUST be on the new flyer is already on the old flyer I have uploaded here. In addition to including: The Volta racing league VOLTA I have uploaded AND the text: 'Very popular, clean and competitive racing league, running for its 4th season. Why not join with a friend? Race times, Mondays, Tuesdays and Wednesdays each at 8pm UK TIME Message below for any questions. (Spacing of information is not important, however all the information in regards to the racing I have just mentioned MUST BE on the flyer, this includes info from old pic, logo and the other info I just mentioned).

It would be beneficial to have lots of dark blue on the flyer and the new flyer to be a lot different to the original flyer I uploaded, but this is not essential.

I apologise if I did not explain very well, any questions, please message me.

The best flyer should look the most attractive to someone that might be interested in joining an online formula one racing league.

I used this website before to create the perfect logo for my Sunday League team last year, and I was very impressed. I look forward to seeing your submissions.

Target Market(s)

No specific target, more something that may attract someone into joining a formula one online racing league

Industry/Entity Type

e sports/formula one

Colors
0054AA
0677BA
7BADD7
CADEEF
E8F1F8

Requirements
Must have
• Read product description please
Should not have
• Ignoring product description!

```html
<!DOCTYPE html>
<html lang="en">
<head>
<meta charset="utf-8">
<title>Volta Racing League</title>
<link rel="stylesheet" href="https://fonts.googleapis.com/css2?family=Montserrat:wght@800&family=Source+Sans+3:wght@400;700;800&display=swap">
<style>
  :root {
    --royal: #0d3bc0;
    --royal-deep: #0a2f9e;
    --band: #0b46e0;
    --navy: #101f6a;
    --ink: #050d2e;
    --white: #ffffff;
    --yellow: #f7ec7a;
    --red: #e8101c;
    --violet: #8a4fb0;
    --check-light: #4a86ff;
    --check-dark: #0a1f8a;
  }
  * { margin: 0; padding: 0; box-sizing: border-box; }
  html, body { width: 1200px; height: 632px; overflow: hidden; background: var(--royal); }
  .flyer {
    position: relative;
    width: 1200px;
    height: 632px;
    overflow: hidden;
    background: radial-gradient(circle at 35% 55%, #1a4fd6 0%, var(--royal) 55%, var(--royal-deep) 100%);
    font-family: "Source Sans 3", "Myriad Pro", sans-serif;
  }
  .backdrop { position: absolute; inset: 0; }
  .title-band {
    position: absolute;
    left: 280px; top: 21px;
    width: 920px; height: 93px;
    background: var(--band);
  }
  .info-panel {
    position: absolute;
    left: 570px; top: 114px;
    width: 630px; height: 240px;
    background: var(--navy);
  }
  .league-title {
    position: absolute;
    left: 296px; top: 30px;
    width: 890px;
    text-align: center;
    font-family: "Montserrat", "Arial Black", sans-serif;
    font-weight: 800;
    font-size: 66px;
    line-height: 80px;
    letter-spacing: 1px;
    color: var(--white);
    white-space: nowrap;
  }
  .line {
    position: absolute;
    left: 330px;
    width: 855px;
    text-align: center;
    white-space: nowrap;
  }
  .pitch { color: var(--yellow); font-weight: 400; font-size: 46px; line-height: 50px; }
  .pitch--one { top: 118px; }
  .pitch--two { top: 182px; }
  .season { top: 236px; color: var(--yellow); font-size: 58px; line-height: 62px; letter-spacing: 0.5px; }
  .invite { top: 304px; color: var(--yellow); font-size: 36px; line-height: 40px; }
  .schedule { color: var(--white); font-size: 66px; line-height: 70px; font-weight: 800; }
  .schedule--one { top: 362px; }
  .schedule--two { top: 432px; }
  .schedule--three { top: 502px; }
  .schedule .lead { font-weight: 400; }
  .contact { top: 588px; color: var(--yellow); font-size: 30px; line-height: 34px; }
  .brand-mark {
    position: absolute;
    left: 10px; top: 187px;
    width: 262px; height: 262px;
    border-radius: 50%;
    background: var(--ink);
    display: flex; align-items: center; justify-content: center;
  }
  .brand-name {
    font-family: "Source Sans 3", sans-serif;
    font-weight: 800;
    font-size: 58px;
    letter-spacing: 2px;
    color: var(--white);
  }
</style>
</head>
<body>
<main class="flyer">
  <svg class="backdrop" width="1200" height="632" viewBox="0 0 1200 632" aria-hidden="true">
    <defs>
      <linearGradient id="arc-red" x1="0" y1="0" x2="0" y2="1">
        <stop offset="0" stop-color="var(--red)"/>
        <stop offset="0.55" stop-color="#c8183a"/>
        <stop offset="1" stop-color="var(--violet)"/>
      </linearGradient>
      <linearGradient id="check-fill" x1="0" y1="0" x2="1" y2="1">
        <stop offset="0" stop-color="var(--check-light)"/>
        <stop offset="1" stop-color="var(--check-dark)"/>
      </linearGradient>
    </defs>
    <g fill="none">
      <circle cx="620" cy="320" r="520" stroke="#1546c8" stroke-width="60" opacity="0.35"/>
      <circle cx="620" cy="320" r="680" stroke="#0c35ad" stroke-width="40" opacity="0.4"/>
    </g>
    <circle cx="-10" cy="330" r="335" fill="none" stroke="url(#arc-red)" stroke-width="22"/>
    <circle cx="-10" cy="330" r="318" fill="none" stroke="#1a0f55" stroke-width="10" opacity="0.7"/>
    <circle cx="-10" cy="330" r="300" fill="none" stroke="#0b2bd8" stroke-width="22"/>
    <g role="img" aria-label="Chequered racing flag waving across the bottom left corner">
      <path d="M0 470 C 90 500 190 530 260 540 C 300 545 320 590 322 632 L 0 632 Z" fill="url(#check-fill)"/>
    </g>
    <g role="img" aria-label="Chequered racing flag in the bottom right corner">
      <path d="M1060 632 C 1070 560 1140 520 1200 500 L 1200 632 Z" fill="url(#check-fill)"/>
    </g>
  </svg>

  <div class="title-band"></div>
  <div class="info-panel"></div>

  <div class="brand-mark"><span class="brand-name">VOLTA</span></div>

  <h1 class="league-title">VOLTA RACING LEAGUE</h1>

  <p class="line pitch pitch--one">Very popular, clean and</p>
  <p class="line pitch pitch--two">competitive racing league,</p>
  <p class="line season">RUNNING FOR ITS 4TH SEASON</p>
  <p class="line invite">Why not join with a friend?</p>

  <p class="line schedule schedule--one"><span class="lead">RACE TIMES,</span> MONDAYS,</p>
  <p class="line schedule schedule--two">TUESDAYS and WEDNESDAYS</p>
  <p class="line schedule schedule--three">EACH AT 8PM UK TIME</p>

  <p class="line contact">Message below for any questions.</p>
</main>
</body>
</html>
```